Transfer Falcon - Cloud Based Data Migration Service for IT Professionals

We are looking for a smart clean website design for an informational site about our services and as a main portal into the service itself. We would like the design completed in WORDPRESS so that it will easily connect with the service.

Transfer Falcon is a cloud based migration service providing (to start with) a online migration tool that we migrate Quillnet Relay mailboxes (email) with all the settings, attachments from one system to another.
The service is aimed at IT professionals, IT companies and IT departments so our customers will be very technology based.

The Service -
IT companies currently migrate email; data and databases. using a very time intensive process which is both expensive and means their customer potentially losses access to its IT for a significant period of time. Additionally there are risks with regards to compatibility between systems and loss of data.
Potential benefits include;
• cost savings
• improved customer service, including reduced downtime
• improved resilience of the process
We are therefore developing cloud based migration software/website which will automate the process, mitigating these issues, as well as providing additional benefits such as the ability to sort and migrate only certain areas of data or certain emails, to check the integrity of the data/emails moved and to also repair corrupted data and emails.
The system will effectively duplicate the data and emails onto the new system over the weeks prior to the completion date. This will enable the IT Company to complete a final synchronisation and then immediately switch over to the new system with no interruption to the end users.
There is also an added benefit that the end users can test the system (with their own data and emails) prior to the switch over date to ensure everything is in place and databases work correctly.
The system will be completely cloud based and therefore easy for the IT Companies to access. They will be able to purchase the use of the system using CoinDrop or credit card and will only need to purchase what they need, this will allow even small local IT companies the facilities which previously would have been cost prohibitive to them.

Some of the sites we like for reference are -
Lanterbox, brightkits, the sky shifter.

We already have a logo design see attached and the website will need to work with this design.
Please message me if you have any questions
We do have the logo in other file formats if required.
Many Thanks

Target Market(s)

IT Sector

Industry/Entity Type

It Service

Number of Pages Required

5+ page

Requirements
Must have
• Front Page
• About Us
• Contact Info
• Blog
• Benefits
• More Information
• Must be Mobile Phone Compatible/friendly
• Log in (button) and support button on all pages (possibley top right)

```html
<!DOCTYPE html>
<html lang="en">
<head>
<meta charset="utf-8">
<title>Transfer Falcon – Cloud Data Migration</title>
<link href="https://fonts.googleapis.com/css2?family=Open+Sans:wght@300;400;600;700;800&display=swap" rel="stylesheet">
<style>
  :root {
    --brand-blue: #0aa6de;
    --ink: #1d1d1d;
    --muted: #b9b9b9;
    --muted-dark: #9a9a9a;
    --panel: #f7f7f7;
    --white: #ffffff;
    --button-dark: #2f2f2f;
    --hero-dark: rgba(16, 24, 30, 0.9);
  }
  * { box-sizing: border-box; margin: 0; padding: 0; }
  html, body { width: 1067px; height: 1200px; overflow: hidden; }
  body {
    position: relative;
    background: var(--white);
    font-family: "Open Sans", Arial, sans-serif;
    color: var(--ink);
  }
  .nowrap { white-space: nowrap; }

  /* Header */
  .site-header { position: absolute; left: 0; top: 0; width: 1067px; height: 128px; background: var(--white); }
  .brand { position: absolute; left: 144px; top: 44px; display: flex; align-items: center; gap: 10px; }
  .brand-dot { width: 30px; height: 30px; border-radius: 50%; background: var(--brand-blue); }
  .brand-name { font-size: 25px; font-weight: 700; color: var(--ink); letter-spacing: 0.5px; }
  .util-btn {
    position: absolute; top: 20px; height: 29px; padding: 0;
    font-size: 11.5px; line-height: 29px; color: var(--white); border-radius: 2px;
    text-align: center; white-space: nowrap;
  }
  .util-login { left: 796px; width: 56px; background: var(--brand-blue); }
  .util-support { left: 860px; width: 63px; background: var(--button-dark); }
  .main-nav a {
    position: absolute; top: 76px; height: 28px; line-height: 28px;
    font-size: 12px; color: #6b6b6b; text-decoration: none; text-transform: uppercase; white-space: nowrap;
  }
  .main-nav .is-active { background: var(--brand-blue); color: var(--white); width: 57px; text-align: center; border-radius: 2px; }

  /* Hero */
  .hero { position: absolute; left: 0; top: 128px; width: 1067px; height: 372px; overflow: hidden; }
  .hero-photo {
    position: absolute; inset: 0;
    background:
      radial-gradient(ellipse at 45% 40%, rgba(255,255,255,0.55), rgba(255,255,255,0) 45%),
      linear-gradient(100deg, #2fa3d8 0%, #6fc6ea 35%, #a6dcf2 55%, #5cbfe8 80%, #aee0f4 100%);
  }
  .hero-hex { position: absolute; left: 204px; top: 44px; width: 226px; height: 256px; }
  .hero-hex-text {
    position: absolute; left: 204px; top: 96px; width: 226px; text-align: center;
    color: var(--white); font-weight: 800; line-height: 1; white-space: nowrap;
  }
  .hero-hex-text .big { font-size: 55px; display: block; }
  .hero-hex-text .mid { font-size: 29px; display: block; margin-top: 6px; }
  .hero-panel {
    position: absolute; left: 553px; top: 85px; width: 368px; height: 212px;
    background: var(--hero-dark); border-radius: 3px; padding: 12px 0 0 29px; color: var(--white);
  }
  .hero-kicker { font-size: 19px; font-weight: 400; line-height: 24px; }
  .hero-title { font-size: 52px; font-weight: 700; line-height: 1; margin-top: 2px; white-space: nowrap; }
  .hero-sub { font-size: 29px; font-weight: 700; line-height: 1; margin-left: 10px; white-space: nowrap; }
  .hero-copy { font-size: 13.5px; line-height: 18px; margin-top: 4px; white-space: nowrap; }
  .hero-actions { display: flex; gap: 14px; margin-top: 12px; }
  .btn-outline, .btn-solid {
    height: 36px; line-height: 34px; padding: 0; font-size: 13.5px; border-radius: 2px;
    text-transform: uppercase; white-space: nowrap; text-align: center;
  }
  .btn-outline { border: 1px solid var(--white); color: var(--white); width: 102px; }
  .btn-solid { background: var(--white); color: var(--ink); width: 102px; border: 1px solid var(--white); }

  /* About */
  .about { position: absolute; left: 0; top: 500px; width: 1067px; height: 124px; text-align: center; }
  .section-title { font-size: 23px; font-weight: 400; color: var(--ink); }
  .about .section-title { margin-top: 26px; text-transform: uppercase; }
  .about-copy { width: 620px; margin: 10px auto 0; font-size: 13px; line-height: 22px; color: var(--muted); }

  /* Blog */
  .blog { position: absolute; left: 0; top: 624px; width: 1067px; height: 300px; background: var(--panel); }
  .blog .section-title { position: absolute; top: 18px; width: 100%; text-align: center; }
  .post { position: absolute; top: 68px; width: 216px; }
  .post-media { width: 216px; height: 123px; }
  .post-title { margin-top: 10px; font-size: 12px; font-weight: 700; color: var(--ink); text-transform: uppercase; white-space: nowrap; }
  .post-excerpt { font-size: 10px; line-height: 14px; color: var(--muted-dark); margin-top: 1px; white-space: nowrap; }
  .post-btn {
    display: inline-block; margin-top: 10px; width: 70px; height: 24px; line-height: 24px; text-align: center;
    background: var(--button-dark); color: var(--white); font-size: 9.5px; text-transform: uppercase; border-radius: 2px; white-space: nowrap;
  }

  /* Benefits */
  .benefits { position: absolute; left: 0; top: 924px; width: 1067px; height: 220px; }
  .benefits .section-title { position: absolute; top: 24px; width: 100%; text-align: center; }
  .benefit-list { position: absolute; top: 76px; list-style: none; }
  .benefit-list li {
    height: 27px; display: flex; align-items: center; gap: 8px;
    font-size: 11.5px; color: var(--muted); white-space: nowrap;
  }
  .benefit-list li::before {
    content: ""; width: 11px; height: 11px; border-radius: 50%; border: 2px solid #555;
  }
  .benefit-list li.is-highlight::before { border-color: var(--brand-blue); }

  /* Footer */
  .site-footer { position: absolute; left: 0; top: 1144px; width: 1067px; height: 56px; background: var(--brand-blue); }
  .copyright { position: absolute; left: 148px; top: 18px; font-size: 14px; color: var(--white); white-space: nowrap; }
  .social { position: absolute; top: 11px; width: 33px; height: 33px; border-radius: 50%; border: 1.5px solid var(--white); }
</style>
</head>
<body>

<header class="site-header">
  <div class="brand">
    <span class="brand-dot"></span>
    <span class="brand-name">Transfer Falcon</span>
  </div>
  <span class="util-btn util-login">LOGIN</span>
  <span class="util-btn util-support">SUPPORT</span>
  <nav class="main-nav">
    <a class="is-active" style="left:563px">Home</a>
    <a style="left:645px">About Us</a>
    <a style="left:721px">Blog</a>
    <a style="left:787px">Benefits</a>
    <a style="left:860px">Contact Us</a>
  </nav>
</header>

<section class="hero">
  <div class="hero-photo" role="img" aria-label="Blurred photo of a businessman touching a glowing blue interface of hexagons with data icons"></div>
  <svg class="hero-hex" viewBox="0 0 226 256" aria-hidden="true">
    <polygon points="113,3 223,66 223,190 113,253 3,190 3,66" fill="#1596cf" stroke="#e6f6fd" stroke-width="4"/>
  </svg>
  <div class="hero-hex-text">
    <span class="big">DATA</span>
    <span class="mid">TRANSFER</span>
    <span class="mid">FALCON</span>
  </div>
  <div class="hero-panel">
    <div class="hero-kicker">WELCOME TO</div>
    <div class="hero-title">TRANSFER</div>
    <div class="hero-sub">FALCON</div>
    <p class="hero-copy">Lorem Ipsum is simply dummy text of the printing<br>and typesetting industry.</p>
    <div class="hero-actions">
      <span class="btn-outline">Read More</span>
      <span class="btn-solid">Buy Now</span>
    </div>
  </div>
</section>

<section class="about">
  <h2 class="section-title">About Us</h2>
  <p class="about-copy">Lorem Ipsum is simply dummy text of the printing and typesetting industry. Lorem Ipsum has been<br>the industry's standard dummy text ever since the 1500s, when an unknown printer</p>
</section>

<section class="blog">
  <h2 class="section-title">Our Blog</h2>
  <article class="post" style="left:184px">
    <div class="post-media" role="img" aria-label="Magnifying glass over green gears and the words data migration" style="background:linear-gradient(135deg,#8a8d90,#d4d6d8 55%,#6f7275)"></div>
    <h3 class="post-title">Lorem Ipsum is simply</h3>
    <p class="post-excerpt">dummy text of the printing and typesetting<br>industry. Lorem Ipsum has been</p>
    <span class="post-btn">Buy Now</span>
  </article>
  <article class="post" style="left:424px">
    <div class="post-media" role="img" aria-label="Tablet showing a dashboard on a desk with printed charts" style="background:linear-gradient(135deg,#eef1f5,#c9d5e3 50%,#2a5fa8 75%,#e8ecf2)"></div>
    <h3 class="post-title">Lorem Ipsum is simply</h3>
    <p class="post-excerpt">dummy text of the printing and typesetting<br>industry. Lorem Ipsum has been</p>
    <span class="post-btn">Buy Now</span>
  </article>
  <article class="post" style="left:667px">
    <div class="post-media" role="img" aria-label="White glossy clouds on a dark background" style="background:radial-gradient(ellipse at 50% 55%,#f2f2f2 0%,#bdbdbd 35%,#2b2b2b 70%)"></div>
    <h3 class="post-title">Lorem Ipsum is simply</h3>
    <p class="post-excerpt">dummy text of the printing and typesetting<br>industry. Lorem Ipsum has been</p>
    <span class="post-btn">Buy Now</span>
  </article>
</section>

<section class="benefits">
  <h2 class="section-title">Our Benefits</h2>
  <ul class="benefit-list" style="left:167px">
    <li>Lorem Ipsum is simply dummy text of</li>
    <li class="is-highlight">the printing and typesetting industry.</li>
    <li>Lorem Ipsum has been the industry's</li>
    <li>standard dummy text ever since the</li>
  </ul>
  <ul class="benefit-list" style="left:421px">
    <li>Lorem Ipsum is simply dummy text of</li>
    <li>the printing and typesetting industry.</li>
    <li>Lorem Ipsum has been the industry's</li>
    <li>standard dummy text ever since the</li>
  </ul>
  <ul class="benefit-list" style="left:684px">
    <li>Lorem Ipsum is simply dummy text of</li>
    <li>the printing and typesetting industry.</li>
    <li>Lorem Ipsum has been the industry's</li>
    <li>standard dummy text ever since the</li>
  </ul>
</section>

<footer class="site-footer">
  <p class="copyright">Copyright © 2016 TransferFalcon.example</p>
  <span class="social" style="left:802px"></span>
  <span class="social" style="left:848px"></span>
  <span class="social" style="left:891px"></span>
</footer>

</body>
</html>
```